Quimby's Yard & Garden Center Business Card Update

I need an updated Business card design for my Lawn and Garden Center. We do Landscaping installs, Lawn Mowing, Snow Removal and also have a Garden Center Retail Division. I uploaded a few of our previous business cards to give an idea of what we are starting with. The main goal of this update is to simplify and modernize the business card, not all of the services that are on the previous cards has to be on the new one but I would still like to highlight our main services. There is also a sample of our logo that Can be used in the design.

Industry/Entity Type

Landscaping

Contact Information for Business Card

Morris Quimby
Morris@Quimbysyardandgarden.example
Business (555) 201-7784
Cell (555) 318-6092

Colors

Designer to choose colors to be used in the design.

Requirements
Must have
• Services Provided :
• Landscaping
• Lawn Maintenance
• Snow Removal
• Garden Center

```html
<!DOCTYPE html>
<html lang="en">
<head>
<meta charset="utf-8">
<title>Quimby's Yard &amp; Garden Center – Business Card</title>
<link href="https://fonts.googleapis.com/css2?family=Montserrat:wght@400;500;700&display=swap" rel="stylesheet">
<style>
  :root{
    --bg:#e9ebe8;
    --paper:#ffffff;
    --forest:#2c5a27;
    --forest-dark:#244b20;
    --lime:#7cc242;
    --ink:#ffffff;
  }
  *{margin:0;padding:0;box-sizing:border-box}
  html,body{width:1200px;height:913px;overflow:hidden;background:var(--bg);font-family:'Montserrat',sans-serif}
  .sheet{position:relative;width:1200px;height:913px}
  .card{position:absolute;left:250px;width:700px;height:400px;border-radius:26px;overflow:hidden;box-shadow:0 6px 18px rgba(0,0,0,.15)}
  .card--front{top:36px;background:var(--paper)}
  .card--back{top:476px;background:var(--forest)}

  /* front */
  .brand{position:absolute;top:70px;right:70px;display:flex;align-items:center;gap:14px}
  .brand__dot{width:34px;height:34px;border-radius:50%;background:var(--forest)}
  .brand__name{font-size:56px;font-weight:700;color:var(--forest);letter-spacing:-.5px}
  .holder{position:absolute;left:60px;top:218px}
  .holder__name{font-size:28px;font-weight:700;color:var(--forest);margin-bottom:12px}
  .contact{list-style:none}
  .contact li{display:flex;align-items:center;gap:12px;font-size:17px;color:var(--forest);line-height:27px}
  .contact svg{width:17px;height:17px;flex:none;fill:var(--forest)}

  /* back */
  .services{position:absolute;left:54px;top:92px;color:var(--ink)}
  .services__title{font-size:19px;font-weight:400;line-height:28px;margin-bottom:2px}
  .services ul{list-style:none}
  .services li{display:flex;align-items:center;gap:6px;font-size:19px;line-height:28px}
  .services svg{width:18px;height:18px;fill:var(--ink);flex:none}
  .storefront{position:absolute;right:40px;top:40px;width:270px;height:190px;border-radius:18px;background:linear-gradient(160deg,#c9ccc9 0%,#8a8d86 45%,#c8a640 75%,#5e7d3a 100%)}
  .business{position:absolute;left:140px;bottom:36px;color:var(--lime)}
  .business__name{font-size:22px;font-weight:700;line-height:28px;padding-bottom:4px;border-bottom:3px solid var(--lime);margin-bottom:6px}
  .business__addr{font-size:19px;line-height:27px}
</style>
</head>
<body>
<main class="sheet">
  <section class="card card--front">
    <div class="brand">
      <span class="brand__dot"></span>
      <span class="brand__name">Quimby's</span>
    </div>
    <div class="holder">
      <h1 class="holder__name">Morris Quimby</h1>
      <ul class="contact">
        <li><svg viewBox="0 0 24 24"><path d="M6.6 10.8a15 15 0 006.6 6.6l2.2-2.2c.3-.3.7-.4 1-.2 1.1.4 2.3.6 3.6.6.6 0 1 .4 1 1V20c0 .6-.4 1-1 1A17 17 0 013 4c0-.6.4-1 1-1h3.5c.6 0 1 .4 1 1 0 1.3.2 2.5.6 3.6.1.3 0 .7-.2 1z"/></svg>(555) 201-7784</li>
        <li><svg viewBox="0 0 24 24"><path d="M7 1h10a2 2 0 012 2v18a2 2 0 01-2 2H7a2 2 0 01-2-2V3a2 2 0 012-2zm0 3v15h10V4zm5 16.2a1 1 0 100 1.6 1 1 0 000-1.6z"/></svg>(555) 318-6092</li>
        <li><svg viewBox="0 0 24 24"><path d="M2 5h20v14H2zm2 2v.5l8 5 8-5V7zm0 2.9V17h16V9.9l-8 5z"/></svg>Morris@Quimbysyardandgarden.example</li>
        <li><svg viewBox="0 0 24 24"><path d="M12 2a10 10 0 100 20 10 10 0 000-20zm6.9 6h-3a15 15 0 00-1.3-3.9A8 8 0 0118.9 8zM12 4c.8 1.2 1.5 2.5 1.9 4h-3.8c.4-1.5 1.100-2.8 1.900-4zM4.3 14a8 8 0 010-4h3.4a16 16 0 000 4zm.8 2h3a15 15 0 001.3 3.9A8 8 0 015.1 16zm3-8h-3a8 8 0 014.3-3.9A15 15 0 008.1 8zM12 20c-.8-1.2-1.5-2.5-1.9-4h3.8c-.4 1.5-1.1 2.8-1.9 4zm2.3-6H9.7a14 14 0 010-4h4.6a14 14 0 010 4zm.3 5.9a15 15 0 001.3-3.9h3a8 8 0 01-4.3 3.9zm1.7-5.9a16 16 0 000-4h3.4a8 8 0 010 4z"/></svg>www.Quimbysyardandgarden.example</li>
      </ul>
    </div>
  </section>

  <section class="card card--back">
    <div class="storefront" role="img" aria-label="Photo of the garden center storefront with flowers on display"></div>
    <div class="services">
      <p class="services__title">Services Provided :</p>
      <ul>
        <li><svg viewBox="0 0 24 24"><path d="M12 2l5 6h-3l5 6h-3l5 6H3l5-6H5l5-6H7z"/></svg>Landscaping</li>
        <li><svg viewBox="0 0 24 24"><path d="M12 2l5 6h-3l5 6h-3l5 6H3l5-6H5l5-6H7z"/></svg>Lawn Maintenance</li>
        <li><svg viewBox="0 0 24 24"><path d="M12 2l5 6h-3l5 6h-3l5 6H3l5-6H5l5-6H7z"/></svg>Snow Removal</li>
        <li><svg viewBox="0 0 24 24"><path d="M12 2l5 6h-3l5 6h-3l5 6H3l5-6H5l5-6H7z"/></svg>Garden Center</li>
      </ul>
    </div>
    <div class="business">
      <p class="business__name">Quimby's Yard &amp; Garden Center</p>
      <p class="business__addr">4820 County Road M, Fairview,<br>Ohio 45999, United States</p>
    </div>
  </section>
</main>
</body>
</html>
```